TRENDY & MODERN BUSINESS CARD DESIGN for Media Company *

I need a minimalistic - clean - modern and professional business card layout and design for MEDIA & PHOTOGRAPHY STUDIO.

We do NOT have a logo, and not really looking for one - but rather excellent typography and design. We would consider the 3 as a focal point.

We do personal and commercial photography.

Target Market(s)

Personal and commercial photography clientele

Contact Information for Business Card

KYT size - from kyt.com / size guidelines are enclosed in the brief

Font styles to use
Sans Serif

Colors
f78f20
eda3c7
cee9f5
0555a3
e667a6
fbf289

Requirements
Must have
• Clean lines - Modern layout
Nice to have
• All blue background as an option - use color palette in brief please.
Should not have
• Old fashion fonts and regular fonts.

```html
<!DOCTYPE html>
<html lang="en">
<head>
<meta charset="utf-8">
<title>Fifth Lens Studio – Business Card</title>
<link rel="stylesheet" href="https://fonts.googleapis.com/css2?family=Open+Sans:wght@400;600;800&display=swap">
<style>
  :root {
    --backdrop: #e4e4e4;
    --navy-deep: #1a2246;
    --navy-mid: #1f2c60;
    --sun-yellow: #fbf289;
    --blush: #e07ab4;
    --card-pink: #e968a2;
    --ink: #1f2a55;
  }
  * { margin: 0; padding: 0; box-sizing: border-box; }
  html, body {
    width: 1200px;
    height: 900px;
    overflow: hidden;
    background: var(--backdrop);
    font-family: "Open Sans", sans-serif;
  }
  .canvas {
    position: relative;
    width: 1200px;
    height: 900px;
  }
  .card {
    position: absolute;
    top: 58px;
    width: 478px;
    height: 716px;
    box-shadow: 0 6px 18px rgba(0, 0, 0, 0.18);
  }
  /* Front */
  .card-front {
    left: 86px;
    background: radial-gradient(ellipse at 50% 48%, var(--navy-mid) 0%, var(--navy-deep) 70%);
    display: flex;
    flex-direction: column;
    align-items: center;
    justify-content: center;
    padding-bottom: 60px;
  }
  .brand-name {
    color: var(--sun-yellow);
    font-weight: 800;
    font-size: 60px;
    line-height: 0.98;
    text-align: center;
    letter-spacing: -1px;
    text-transform: uppercase;
  }
  .tagline {
    margin-top: 20px;
    font-weight: 400;
    font-size: 16px;
    letter-spacing: 1.5px;
    text-transform: uppercase;
    color: var(--blush);
  }
  /* Back */
  .card-back {
    left: 655px;
    background: var(--card-pink);
    color: var(--ink);
  }
  .identity {
    position: absolute;
    top: 178px;
    left: 0;
    width: 100%;
    text-align: center;
  }
  .person-name {
    font-size: 26px;
    font-weight: 600;
  }
  .person-role {
    margin-top: 6px;
    font-size: 17px;
  }
  .contact-list {
    position: absolute;
    top: 334px;
    left: 112px;
    list-style: none;
    font-size: 19px;
    line-height: 25px;
  }
  .contact-item {
    display: flex;
    align-items: flex-start;
    margin-bottom: 19px;
  }
  .contact-icon {
    width: 26px;
    height: 22px;
    margin-right: 16px;
    margin-top: 2px;
    flex-shrink: 0;
    fill: var(--ink);
  }
  .contact-icon .outline {
    fill: none;
    stroke: var(--ink);
    stroke-width: 2.4;
  }
</style>
</head>
<body>
<main class="canvas">
  <section class="card card-front">
    <h1 class="brand-name">Fifth Lens<br>Studio</h1>
    <p class="tagline">Real Moments. Lasting Frames.</p>
  </section>

  <section class="card card-back">
    <header class="identity">
      <h2 class="person-name">Marisol Vega</h2>
      <p class="person-role">Founder &amp; Media Director</p>
    </header>
    <ul class="contact-list">
      <li class="contact-item">
        <svg class="contact-icon" viewBox="0 0 26 22" aria-hidden="true">
          <path d="M5 2c1-1 2-1 3 0l3 4c.6.8.4 1.6-.2 2.2L9.5 9.5c1 2.3 2.7 4 5 5l1.3-1.3c.6-.6 1.4-.8 2.2-.2l3.5 2.6c1 .8 1 1.8 0 2.8l-1.5 1.5C17 22 3 10 3.6 4.4z"/>
        </svg>
        <span>(305) 555-0142</span>
      </li>
      <li class="contact-item">
        <svg class="contact-icon" viewBox="0 0 26 22" aria-hidden="true">
          <path class="outline" d="M2 4h22v15H2z M4 6l9 7 9-7"/>
        </svg>
        <span>marisol@fifthlensstudio.com</span>
      </li>
      <li class="contact-item">
        <svg class="contact-icon" viewBox="0 0 26 22" aria-hidden="true">
          <path d="M13 1L1 11h3v10h7v-6h4v6h7V11h3z"/>
        </svg>
        <span>2400 Coral Way<br>4th Floor<br>Miami, FL 33145</span>
      </li>
    </ul>
  </section>
</main>
</body>
</html>
```